Graphic Design Project

We need a single page design that will be used as a regular white paper, providing communication advice & techniques.

We have an example that needs upgrading to look more professional and exciting.

Logo and icons will be provided.

Image provided for this example but will need to be able to add and remove new images relative to each new white paper.

Design will need to be on a format that is easily editable and can be converted into a PDF document. e.g MS Word.

Target Market(s)

Existing and potential corporate individuals and organisations

Industry/Entity Type

Communication

Requirements
Must have
• Logo, Icons & web address

```html
<!DOCTYPE html>
<html lang="en">
<head>
<meta charset="utf-8">
<title>The Seven Deadly Sins of Presenting with Slides</title>
<link href="https://fonts.googleapis.com/css2?family=Oswald:wght@500;600&family=Arimo:wght@400;700&display=swap" rel="stylesheet">
<style>
  :root {
    --charcoal: #3a3a3c;
    --heading: #3b3b3d;
    --body: #2d2d2f;
    --green: #8cc63f;
    --rule: #c9c9c9;
    --footer-bg: #e6e6e6;
    --footer-band: #cfcfcf;
    --brown: #7a6a58;
    --orange: #f7941d;
    --white: #ffffff;
  }
  * { margin: 0; padding: 0; box-sizing: border-box; }
  html, body { width: 849px; height: 1200px; overflow: hidden; background: var(--white); }
  .page { position: relative; width: 849px; height: 1200px; font-family: "Arimo", Arial, sans-serif; color: var(--body); }

  .masthead { position: absolute; left: 0; top: 0; width: 849px; height: 74px; background: var(--charcoal); }
  .masthead h1 { position: absolute; left: 37px; top: 12px; font-family: "Oswald", "Arial Narrow", sans-serif; font-weight: 600; font-size: 37px; line-height: 48px; color: var(--white); letter-spacing: 0.2px; }

  .intro { position: absolute; left: 26px; top: 80px; width: 465px; height: 208px; background: var(--green); padding: 10px 12px 0 12px; color: var(--white); }
  .intro h2 { font-family: "Oswald", "Arial Narrow", sans-serif; font-weight: 600; font-size: 17px; line-height: 20px; text-transform: uppercase; }
  .intro p { margin-top: 6px; font-size: 14.3px; line-height: 18.6px; text-align: justify; }

  .intro-visual { position: absolute; left: 496px; top: 80px; width: 328px; height: 208px; background: radial-gradient(ellipse at 60% 40%, #e8e8e8 0%, #b9b9b9 55%, #8c8c8c 100%); }

  .sin { position: absolute; left: 26px; width: 800px; padding-left: 12px; }
  .sin::before { content: ""; position: absolute; left: 0; top: 2px; width: 9px; height: 56px; background: var(--green); }
  .sin::after { content: ""; position: absolute; left: 0; top: 58px; width: 1px; height: 48px; background: var(--rule); }
  .sin.last::after { display: none; }
  .sin h3 { font-family: "Oswald", "Arial Narrow", sans-serif; font-weight: 500; font-size: 18px; line-height: 22px; color: var(--heading); text-transform: uppercase; }
  .sin p { margin-top: 2px; font-size: 14.6px; line-height: 19.4px; }

  .footer-top { position: absolute; left: 26px; top: 1075px; width: 798px; height: 11px; background: var(--footer-band); }
  .footer { position: absolute; left: 26px; top: 1086px; width: 798px; height: 102px; background: var(--footer-bg); }
  .footer-bottom { position: absolute; left: 26px; top: 1189px; width: 798px; height: 11px; background: var(--footer-band); }

  .brand { position: absolute; left: 12px; top: 32px; font-size: 22px; font-weight: 700; color: var(--charcoal); letter-spacing: -0.3px; }
  .divider { position: absolute; top: 22px; width: 1px; height: 58px; background: #9a9a9a; }
  .service { position: absolute; top: 30px; display: flex; align-items: center; gap: 6px; font-size: 13px; line-height: 16px; color: var(--charcoal); }
  .service .dot { width: 40px; height: 40px; border-radius: 50%; border: 3px solid var(--white); }
  .visit { position: absolute; left: 530px; top: 30px; font-size: 14px; line-height: 20px; font-weight: 700; color: var(--charcoal); }
</style>
</head>
<body>
<div class="page">
  <header class="masthead">
    <h1>THE SEVEN DEADLY SINS OF PRESENTING WITH SLIDES</h1>
  </header>

  <section class="intro">
    <h2>There is an increasing expectation for organisational professionals to communicateusing</h2>
    <p>such as SlideForge, Stagecraft and Pivotly, all great tools for enhancing our message. Yet we have all sat through presentations where technology takes over, working against the presenter where amongst the fumbling and mumbling the message is lost. Enhance your message, improve credibility and connect with your audience by avoiding these seven deadly sins of presenting with slides:</p>
  </section>
  <div class="intro-visual" role="img" aria-label="Silhouette paper-chain figures facing a speaker at a podium"></div>

  <article class="sin" style="top:308px">
    <h3>Rely onTechnology</h3>
    <p>Batteries go flat, software crashes, lights go out and speakers breakdown, we all know it and yet we rarely give ourselves enough time to set up, test and re-test our presentation tools.</p>
  </article>
  <article class="sin" style="top:413px">
    <h3>Read your slides</h3>
    <p>Slides are fantastic, we love them for their ability to enhance the spoken word but they are not the message itself. Reading your slides will kill your credibility and engagement, please don’t do it!</p>
  </article>
  <article class="sin" style="top:518px">
    <h3>Dim the lights</h3>
    <p>Low light sends us a subconscious signal to relax and prepare for sleep, probably not the emotional state you want your audience in! Wherever possible set your room with natural light that doesn’t glare the screen.</p>
  </article>
  <article class="sin" style="top:624px">
    <h3>Appoint a ‘slider’</h3>
    <p>A Slider is a person who is asked to press the ‘Enter’ key to move the slides on your behalf. Lovely people but a complete distraction and incapable of working in sync with your natural rhythm. Insist on a wireless slider clicker, discreet and highly effective.</p>
  </article>
  <article class="sin" style="top:747px">
    <h3>Deliver a monologue</h3>
    <p>Effective communication is a two way street.&nbsp; Where possible move away from your slides,<br>even blank the screen to engage with your audience.</p>
  </article>
  <article class="sin" style="top:850px">
    <h3>Get stuck in the mud</h3>
    <p>Being conscious of the projector light is a good thing but don’t get physically stuck in one<br>position while trying to avoid a shadow on the screen.</p>
  </article>
  <article class="sin last" style="top:955px">
    <h3>Using your slides as a prompt</h3>
    <p>If you don’t know what slide is next you will fall into the ‘click, pause, deliver’ trap where you are reliant<br>on your slides for what to say next. Know your stuff and create verbal segways between slides to deliver<br>consistency and flow.</p>
  </article>

  <div class="footer-top"></div>
  <footer class="footer">
    <div class="brand">Brightline</div>
    <div class="divider" style="left:176px"></div>
    <div class="service" style="left:182px"><span class="dot" style="background:var(--green)"></span><span>Corporate<br>Training</span></div>
    <div class="divider" style="left:295px"></div>
    <div class="service" style="left:301px"><span class="dot" style="background:var(--brown)"></span><span>Coaching</span></div>
    <div class="divider" style="left:404px"></div>
    <div class="service" style="left:410px"><span class="dot" style="background:var(--orange)"></span><span>Public<br>Workshop</span></div>
    <div class="divider" style="left:522px"></div>
    <div class="visit">For more information visit:<br>www.brightlinecomms.com.au</div>
  </footer>
  <div class="footer-bottom"></div>
</div>
</body>
</html>
```